qTorvanix - A forward thinking technology company in the greater Silicon Valley

A .ppt slide deck for a software consulting company. This slide deck will be used for project kick off meetings, sales proposals, and presentations to large audiences that report progress on a variety of projects. It should catch the eye with appealing creativity. Allow for flexibility in space and display. Project well both virtually and in person under varying light conditions. The finished product should give the impression that we are a custom shop but balance in appeal to larger, more traditional companies.

Review of the designs has been delayed due to holiday travel. Thank you for your submissions. I look forward to getting back to you the week of December 3rd.

Target Market(s)

We are an innovative technology company in the greater Silicon Valley. We design and build custom business analytics tools for large, retail corporations. Our solutions deal primarily in the supply chain space but we are leaning towards commercial construction and telecommunications industries. We are targeting prospective clients interested in machine learning and artificial intelligence. Our customers know quality and will pay for a custom solution that exceeds their expectations.

Industry/Entity Type

Business Software

Font styles to use
Sans Serif

Colors

Designer to choose colors to be used in the design.

Requirements
Must have
• Color, graphics, and photos. Multiple different template pages to appeal for graphs, pictures, text, or timelines.
Should not have
• Anything that resembles a "fidget spinner."

```html
<!DOCTYPE html>
<html lang="en">
<head>
<meta charset="utf-8">
<title>qTorvanix – Presentation Deck Overview</title>
<link rel="stylesheet" href="https://fonts.googleapis.com/css2?family=Open+Sans:wght@400;600;700&display=swap">
<style>
:root{
  --green:#76983a;
  --green-dark:#5f7f2a;
  --green-mid:#9ab85e;
  --green-light:#c9dca6;
  --green-pale:#e4eed2;
  --ink:#222;
  --ink-soft:#555;
  --grey-line:#d8d8d8;
  --grey-bg:#e9e9e9;
  --white:#fff;
  --red-link:#b03a3a;
}
*{box-sizing:border-box;margin:0;padding:0}
html,body{width:1200px;height:3364px;overflow:hidden;background:var(--grey-bg)}
body{font-family:"Open Sans",Arial,sans-serif;color:var(--ink);position:relative}

/* hero */
.hero{position:absolute;left:0;top:0;width:1200px;height:670px;overflow:hidden}
.hero-photo{position:absolute;inset:0;background:linear-gradient(160deg,#6f7378 0%,#3a3d41 45%,#1f2124 100%)}
.hero-banner{position:absolute;left:168px;top:0;width:864px;height:292px}
.hero-brand{position:absolute;left:0;right:0;top:102px;text-align:center}
.hero-brand .brand-name{font-size:70px;letter-spacing:3px;color:#6a6a6a;font-weight:400}
.hero-brand .brand-mark{display:inline-block;width:38px;height:38px;background:var(--green);margin-right:22px;vertical-align:6px}
.hero-tagline{position:absolute;left:0;right:0;top:200px;text-align:center;color:var(--green);font-size:33px;font-weight:600}

/* deck grid */
.deck{position:absolute;left:0;top:672px;width:1200px;height:2692px;display:grid;
  grid-template-columns:598px 598px;column-gap:4px;grid-template-rows:repeat(8,334px);row-gap:2.57px}
.slide{position:relative;background:var(--white);overflow:hidden}
.title{position:absolute;left:0;right:0;text-align:center;font-size:24px;font-weight:600;color:var(--ink)}
.title em{font-style:normal;color:var(--green)}
.copy{font-size:6.4px;line-height:1.38;color:#333}
.copy u{color:var(--red-link);text-decoration:underline}
.photo{position:absolute}
.footer-logo{position:absolute;left:12px;bottom:8px;font-size:8px;color:#6a6a6a;display:flex;align-items:center;gap:4px}
.footer-logo i{display:block;width:6px;height:6px;background:var(--green)}

/* contact */
.contact-logo{position:absolute;left:0;right:0;top:78px;text-align:center}
.contact-logo .brand-name{font-size:20px;color:#6a6a6a;letter-spacing:1px}
.contact-logo .brand-mark{display:inline-block;width:12px;height:12px;background:var(--green);margin-right:8px}
.contact-logo .tag{display:block;font-size:7px;color:var(--green);font-weight:600}
.contact-text{position:absolute;left:160px;width:280px;top:140px;text-align:center}
.contact-row{position:absolute;left:40px;right:40px;top:222px;display:flex;justify-content:space-between}
.contact-item{width:120px;text-align:center;font-size:6.6px;color:#333}
.contact-item svg{display:block;margin:0 auto 8px;width:26px;height:26px}

/* break */
.break-box{position:absolute;left:150px;top:134px;width:270px;height:54px;border:2px solid var(--white);
  color:var(--white);font-size:27px;text-align:center;line-height:50px;letter-spacing:1px;background:rgba(0,0,0,.25)}

/* numbered lists */
.num-grid{position:absolute;display:grid}
.num-item{display:flex;gap:6px}
.num-item b{font-size:17px;font-weight:400;color:#333;line-height:1}
.num-item .copy strong{display:block;font-weight:600;color:#222}
.green-band{position:absolute;left:0;right:0;bottom:0;height:70px;background:var(--green);color:var(--white);
  font-weight:700;font-size:12.5px;text-align:center;padding-top:18px;line-height:1.45}

/* icon grid */
.icon-grid{position:absolute;left:30px;right:30px;top:80px;display:grid;grid-template-columns:repeat(4,1fr);row-gap:18px}
.icon-cell{text-align:center}
.icon-cell svg{width:26px;height:26px;display:block;margin:0 auto 8px}
.icon-cell .copy{width:90px;margin:0 auto}

/* pricing */
.price-table{position:absolute;left:20px;right:20px;top:88px;border-collapse:collapse;width:558px;font-size:9px;text-align:center}
.price-table th{color:var(--white);font-weight:600;height:26px;font-size:9px}
.price-table th.c1,.price-table th.c4{background:var(--green)}
.price-table th.c2,.price-table th.c3{background:var(--green-light)}
.price-table td{height:27px;border-bottom:1px solid var(--grey-line)}
.price-table tr.plan td{background:#ececec;font-weight:700;font-size:10px}
.price-table td:nth-child(odd){background:#f6f6f6}
.price-band{position:absolute;left:20px;width:558px;bottom:14px;height:10px;background:var(--green)}

/* timeline */
.timeline-line{position:absolute;left:20px;right:20px;top:120px;height:3px;background:#bbb}
.timeline{position:absolute;left:20px;right:20px;top:86px;display:grid;grid-template-columns:repeat(5,1fr)}
.tl-step{text-align:center}
.tl-year{display:inline-block;background:var(--green);color:var(--white);font-size:9px;font-weight:700;padding:3px 12px;border-radius:10px}
.tl-dot{width:38px;height:38px;border:4px solid var(--green);border-radius:50%;background:var(--white);margin:6px auto 0}
.tl-stem{width:3px;height:24px;background:var(--green);margin:0 auto}
.tl-step .copy{width:95px;margin:8px auto 0}

/* team */
.team-band{position:absolute;left:0;right:0;top:86px;height:64px;background:var(--green)}
.team{position:absolute;left:30px;right:30px;top:66px;display:grid;grid-template-columns:repeat(3,1fr)}
.member{text-align:center}
.avatar{width:104px;height:104px;border-radius:50%;margin:0 auto;border:4px solid var(--white)}
.member .name{font-size:8px;font-weight:700;margin-top:8px}
.member .role{font-size:7px;font-style:italic;color:#444}
.member .copy{width:120px;margin:6px auto 0;text-align:center}

/* pills */
.pill-list{position:absolute;left:210px;right:20px;top:86px;display:flex;flex-direction:column;gap:16px}
.pill{height:42px;border-radius:21px;display:flex;align-items:center;gap:18px;padding-left:6px;font-size:8px}
.pill span{width:32px;height:32px;border-radius:50%;border:2px solid var(--white);color:var(--white);display:flex;align-items:center;justify-content:center;font-size:13px}
.pill.p1{background:var(--green);color:var(--white)}
.pill.p2{background:var(--green-mid);color:#2a3514}
.pill.p3{background:var(--green-light);color:#2a3514}
.pill.p3 span{border-color:var(--green);color:var(--green)}

/* venn */
.venn{position:absolute;left:36px;top:64px;width:240px;height:250px}
.venn-label{position:absolute;color:var(--white);font-size:10px;text-align:center;line-height:1.3}

/* thank you */
.thanks-panel{position:absolute;left:112px;top:0;width:374px;height:292px;background:rgba(245,245,245,.95)}
.thanks-mark{position:absolute;left:0;right:0;top:78px;text-align:center}
.thanks-mark i{display:inline-block;width:46px;height:46px;background:var(--green)}
.thanks-word{position:absolute;left:0;right:0;top:150px;text-align:center;font-size:32px;font-weight:700;color:var(--green)}
.thanks-logo{position:absolute;left:0;right:0;top:196px;text-align:center;font-size:10px;color:#6a6a6a}
</style>
</head>
<body>

<header class="hero">
  <div class="hero-photo" role="img" aria-label="Photo of a laptop keyboard on a desk in soft light"></div>
  <svg class="hero-banner" viewBox="0 0 864 292" aria-hidden="true"><polygon points="0,0 864,0 864,230 432,292 0,230" fill="#fff" fill-opacity="0.86"/></svg>
  <div class="hero-brand"><span class="brand-mark"></span><span class="brand-name">qTorvanix</span></div>
  <p class="hero-tagline">Your Partner for Innovative Software Solutions</p>
</header>

<main class="deck">

  <!-- Contact -->
  <section class="slide">
    <h2 class="title" style="top:44px">Get <em>in Touch</em></h2>
    <div class="contact-logo"><span class="brand-mark"></span><span class="brand-name">qTorvanix</span><span class="tag">Your Partner for Innovative Software Solutions</span></div>
    <p class="copy contact-text">Lorem ipsum dolor sit amet, consectetur adipiscing elit, sed do eiusmod tempor incididunt ut labore et dolore magna aliqua. Ut enim ad minim veniam, quis nostrud exercitation ullamco laboris nisi ut aliquip ex ea commodo consequat.</p>
    <div class="contact-row">
      <div class="contact-item"><svg viewBox="0 0 24 24"><rect x="2" y="5" width="20" height="14" fill="#222"/><path d="M2 5l10 8 10-8" stroke="#fff" stroke-width="1.6" fill="none"/></svg>Company email</div>
      <div class="contact-item"><svg viewBox="0 0 24 24"><path d="M6 2l4 4-2 3c1 3 4 6 7 7l3-2 4 4-3 4C10 22 2 14 2 5z" fill="#222"/></svg>+1 (555) 010 2417</div>
      <div class="contact-item"><svg viewBox="0 0 24 24"><path d="M12 1a7 7 0 0 0-7 7c0 6 7 15 7 15s7-9 7-15a7 7 0 0 0-7-7z" fill="#222"/><circle cx="12" cy="8" r="2.6" fill="#fff"/></svg><u style="color:var(--red-link)">48 Orchard Lane</u>, Austin, USA</div>
      <div class="contact-item"><svg viewBox="0 0 24 24" fill="none" stroke="#222" stroke-width="1.8"><circle cx="12" cy="12" r="10"/><ellipse cx="12" cy="12" rx="4.5" ry="10"/><path d="M2 12h20M4 7h16M4 17h16"/></svg>https://qtorvanix.example</div>
    </div>
  </section>

  <!-- Break -->
  <section class="slide">
    <div class="photo" style="inset:0;background:linear-gradient(120deg,#1c2127,#33302a 50%,#151a1e)" role="img" aria-label="Dark photo of source code on a screen"></div>
    <div class="break-box">BREAK SECTION</div>
  </section>

  <!-- About company -->
  <section class="slide">
    <h2 class="title" style="top:28px;left:24px;text-align:left;font-size:23px">About <em>qTorvanix</em></h2>
    <div class="copy" style="position:absolute;left:24px;top:78px;width:250px">
      <p>Lorem ipsum dolor sit amet, consectetur adipiscing elit, sed do eiusmod tempor incididunt ut labore et dolore magna aliqua. Ut enim ad minim veniam, quis nostrud exercitation ullamco laboris nisi ut aliquip ex ea commodo consequat. Lorem ipsum dolor sit amet, consectetur adipiscing elit, sed do eiusmod tempor incididunt ut labore et dolore magna aliqua.</p><br>
      <p>Aliquip ex ea commodo consequat. Lorem ipsum dolor sit amet, consectetur adipiscing elit, sed do eiusmod tempor incididunt ut labore et dolore magna aliqua. Ut enim ad minim veniam, quis nostrud exercitation ullamco laboris nisi.</p>
    </div>
    <div class="photo" style="left:302px;top:0;width:296px;height:206px;background:linear-gradient(135deg,#5c646c,#2d3238 60%,#8a8f94)" role="img" aria-label="Photo of a laptop showing an analytics dashboard"></div>
    <div class="footer-logo"><i></i>qTorvanix</div>
  </section>

  <!-- About business -->
  <section class="slide">
    <h2 class="title" style="top:34px;left:36px;text-align:left;font-size:23px">About <em>Our Business</em></h2>
    <div class="copy" style="position:absolute;left:36px;top:80px;width:250px">
      <p>Lorem ipsum dolor sit amet, consectetur adipiscing elit, sed do eiusmod tempor incididunt ut labore et dolore magna aliqua. Ut enim ad minim veniam, quis nostrud exercitation ullamco laboris nisi ut aliquip ex ea commodo consequat. Lorem ipsum dolor sit amet, consectetur adipiscing elit, sed do eiusmod tempor incididunt.</p><br>
      <p>Lorem ipsum dolor sit amet, consectetur adipiscing elit, sed do eiusmod tempor incididunt ut labore et dolore magna aliqua.</p><br>
      <p>Aliquip ex ea commodo consequat. Lorem ipsum dolor sit amet, consectetur adipiscing elit, sed do eiusmod tempor incididunt ut labore. Ut enim ad minim veniam, quis nostrud exercitation ullamco.</p>
    </div>
    <div class="photo" style="left:322px;top:0;width:276px;height:334px;background:linear-gradient(150deg,#7d8388,#3c4146 55%,#6b7076)" role="img" aria-label="Photo of a person working on a laptop with charts"></div>
  </section>

  <!-- Text two columns -->
  <section class="slide">
    <h2 class="title" style="top:130px;left:34px;text-align:left;font-size:21px">Lorem ipsum <em>dolor</em></h2>
    <p class="copy" style="position:absolute;left:244px;top:36px;width:150px">Lorem ipsum dolor sit amet, consectetur adipiscing elit, sed do eiusmod tempor incididunt ut labore et dolore magna aliqua. Ut enim ad minim veniam, quis nostrud exercitation ullamco laboris nisi ut aliquip ex ea commodo consequat. Lorem ipsum dolor sit amet, consectetur adipiscing elit, sed do eiusmod tempor incididunt ut labore et dolore magna aliqua. Lorem ipsum dolor sit amet, consectetur adipiscing elit. Ut enim ad minim veniam, quis nostrud exercitation ullamco laboris nisi ut aliquip ex ea commodo consequat. Lorem ipsum dolor sit amet, consectetur adipiscing elit, sed do eiusmod tempor incididunt ut labore et dolore magna aliqua.</p>
    <p class="copy" style="position:absolute;left:410px;top:36px;width:150px">Lorem ipsum dolor sit amet, consectetur adipiscing elit, sed do eiusmod tempor incididunt ut labore et dolore magna aliqua. Ut enim ad minim veniam, quis nostrud exercitation ullamco laboris nisi ut aliquip ex ea commodo consequat. Lorem ipsum dolor sit amet, consectetur adipiscing elit, sed do eiusmod tempor incididunt ut labore et dolore magna aliqua. Lorem ipsum dolor sit amet, consectetur adipiscing elit. Ut enim ad minim veniam, quis nostrud exercitation ullamco laboris nisi ut aliquip ex ea commodo consequat. Lorem ipsum dolor sit amet, consectetur adipiscing elit, sed do eiusmod tempor.</p>
    <div class="footer-logo"><i></i>qTorvanix</div>
  </section>

  <!-- Text three columns -->
  <section class="slide">
    <h2 class="title" style="top:16px;font-size:21px">Lorem ipsum <em>dolor</em></h2>
    <p class="copy" style="position:absolute;left:46px;top:58px;width:150px">Lorem ipsum dolor sit amet, consectetur adipiscing elit, sed do eiusmod tempor incididunt ut labore et dolore magna aliqua. Ut enim ad minim veniam, quis nostrud exercitation ullamco laboris nisi. Lorem ipsum dolor sit amet, consectetur adipiscing elit, sed do eiusmod tempor incididunt ut labore et dolore magna aliqua. Ut enim ad minim veniam, quis nostrud exercitation ullamco laboris nisi ut aliquip ex ea commodo.</p>
    <p class="copy" style="position:absolute;left:216px;top:58px;width:150px">Lorem ipsum dolor sit amet, consectetur adipiscing elit, sed do eiusmod tempor incididunt ut labore et dolore magna aliqua. Ut enim ad minim veniam, quis nostrud exercitation ullamco laboris nisi ut aliquip ex ea commodo consequat. Lorem ipsum dolor sit amet, consectetur adipiscing elit, sed do eiusmod tempor incididunt ut labore et dolore magna aliqua. Ut enim ad minim veniam.</p>
    <p class="copy" style="position:absolute;left:386px;top:58px;width:150px">Lorem ipsum dolor sit amet, consectetur adipiscing elit, sed do eiusmod tempor incididunt ut labore et dolore magna aliqua. Ut enim ad minim veniam, quis nostrud exercitation ullamco laboris nisi ut aliquip ex ea commodo consequat. Lorem ipsum dolor sit amet, consectetur adipiscing elit, sed do eiusmod tempor incididunt ut labore et dolore magna aliqua. Ut enim ad minim veniam.</p>
  </section>

  <!-- Six items -->
  <section class="slide">
    <h2 class="title" style="top:44px">Lorem ipsum <em>dolor</em></h2>
    <div class="num-grid" style="left:26px;right:30px;top:120px;grid-template-columns:repeat(3,1fr);row-gap:40px">
      <div class="num-item"><b>01</b><p class="copy"><strong>Lorem ipsum dolor</strong>Lorem ipsum dolor sit<br><u>amet, consectetur</u><br><u>adipiscing elit</u>, sed<br><u>eiusmod tempor</u>.</p></div>
      <div class="num-item"><b>02</b><p class="copy"><strong>Lorem ipsum dolor</strong>Lorem ipsum dolor sit<br><u>amet, consectetur</u><br><u>adipiscing elit</u>, sed<br><u>eiusmod tempor</u>.</p></div>
      <div class="num-item"><b>03</b><p class="copy"><strong>Lorem ipsum dolor</strong>Lorem ipsum dolor sit<br><u>amet, consectetur</u><br><u>adipiscing elit</u>, sed<br><u>eiusmod tempor</u>.</p></div>
      <div class="num-item"><b>04</b><p class="copy"><strong>Lorem ipsum dolor</strong>Lorem ipsum dolor sit<br><u>amet, consectetur</u><br><u>adipiscing elit</u>, sed<br><u>eiusmod tempor</u>.</p></div>
      <div class="num-item"><b>05</b><p class="copy"><strong>Lorem ipsum dolor</strong>Lorem ipsum dolor sit<br><u>amet, consectetur</u><br><u>adipiscing elit</u>, sed<br><u>eiusmod tempor</u>.</p></div>
      <div class="num-item"><b>06</b><p class="copy"><strong>Lorem ipsum dolor</strong>Lorem ipsum dolor sit<br><u>amet, consectetur</u><br><u>adipiscing elit</u>, sed<br><u>eiusmod tempor</u>.</p></div>
    </div>
    <div class="footer-logo"><i></i>qTorvanix</div>
  </section>

  <!-- Eight items with band -->
  <section class="slide">
    <h2 class="title" style="top:18px">Lorem ipsum <em>dolor</em></h2>
    <div class="num-grid" style="left:10px;right:10px;top:80px;grid-template-columns:repeat(4,1fr);row-gap:22px">
      <div class="num-item"><b>01</b><p class="copy"><strong>Lorem ipsum dolor</strong>Lorem ipsum dolor sit<br><u>amet, consectetur</u><br><u>adipiscing elit</u>, sed<br><u>eiusmod tempor</u>.</p></div>
      <div class="num-item"><b>02</b><p class="copy"><strong>Lorem ipsum dolor</strong>Lorem ipsum dolor sit<br><u>amet, consectetur</u><br><u>adipiscing elit</u>, sed<br><u>eiusmod tempor</u>.</p></div>
      <div class="num-item"><b>03</b><p class="copy"><strong>Lorem ipsum dolor</strong>Lorem ipsum dolor sit<br><u>amet, consectetur</u><br><u>adipiscing elit</u>, sed<br><u>eiusmod tempor</u>.</p></div>
      <div class="num-item"><b>04</b><p class="copy"><strong>Lorem ipsum dolor</strong>Lorem ipsum dolor sit<br><u>amet, consectetur</u><br><u>adipiscing elit</u>, sed<br><u>eiusmod tempor</u>.</p></div>
      <div class="num-item"><b>05</b><p class="copy"><strong>Lorem ipsum dolor</strong>Lorem ipsum dolor sit<br><u>amet, consectetur</u><br><u>adipiscing elit</u>, sed<br><u>eiusmod tempor</u>.</p></div>
      <div class="num-item"><b>06</b><p class="copy"><strong>Lorem ipsum dolor</strong>Lorem ipsum dolor sit<br><u>amet, consectetur</u><br><u>adipiscing elit</u>, sed<br><u>eiusmod tempor</u>.</p></div>
      <div class="num-item"><b>07</b><p class="copy"><strong>Lorem ipsum dolor</strong>Lorem ipsum dolor sit<br><u>amet, consectetur</u><br><u>adipiscing elit</u>, sed<br><u>eiusmod tempor</u>.</p></div>
      <div class="num-item"><b>08</b><p class="copy"><strong>Lorem ipsum dolor</strong>Lorem ipsum dolor sit<br><u>amet, consectetur</u><br><u>adipiscing elit</u>, sed<br><u>eiusmod tempor</u>.</p></div>
    </div>
    <p class="green-band">Lorem ipsum dolor sit amet, consectetur adipiscing elit,<br>sed do eiusmod tempor</p>
  </section>

  <!-- Icon grid -->
  <section class="slide">
    <h2 class="title" style="top:16px">Lorem ipsum <em>dolor</em></h2>
    <div class="icon-grid">
      <div class="icon-cell"><svg viewBox="0 0 24 24" fill="none" stroke="#333" stroke-width="1.6"><circle cx="9" cy="12" r="4"/><path d="M9 5v2M9 17v2M2 12h2M14 12h2M4 7l1.5 1.5M12.5 15.5L14 17M4 17l1.5-1.5M12.5 8.5L14 7"/><circle cx="18" cy="6" r="2.5"/></svg><p class="copy"><strong>Lorem ipsum dolor</strong><br>Lorem ipsum dolor sit amet, consectetur adipiscing elit, sed do eiusmod tempor</p></div>
      <div class="icon-cell"><svg viewBox="0 0 24 24" fill="none" stroke="#333" stroke-width="1.6"><path d="M12 3a6 6 0 0 0-3.5 10.9V17h7v-3.1A6 6 0 0 0 12 3zM9.5 20h5"/><path d="M12 0v1M3 9H2M22 9h-1"/></svg><p class="copy"><strong>Lorem ipsum dolor</strong><br>Lorem ipsum dolor sit amet, consectetur adipiscing elit, sed do eiusmod tempor</p></div>
      <div class="icon-cell"><svg viewBox="0 0 24 24" fill="none" stroke="#333" stroke-width="1.6"><circle cx="12" cy="12" r="7"/><circle cx="12" cy="12" r="2.5"/><path d="M12 1v6M12 17v6M1 12h6M17 12h6"/></svg><p class="copy"><strong>Lorem ipsum dolor</strong><br>Lorem ipsum dolor sit amet, consectetur adipiscing elit, sed do eiusmod tempor</p></div>
      <div class="icon-cell"><svg viewBox="0 0 24 24" fill="none" stroke="#333" stroke-width="1.6"><circle cx="15" cy="9" r="4"/><circle cx="7" cy="16" r="3"/><path d="M15 3v2M15 13v2M9 9h2M19 9h2"/></svg><p class="copy"><strong>Lorem ipsum dolor</strong><br>Lorem ipsum dolor sit amet, consectetur adipiscing elit, sed do eiusmod tempor</p></div>
      <div class="icon-cell"><svg viewBox="0 0 24 24" fill="none" stroke="#333" stroke-width="1.6"><path d="M12 3a6 6 0 0 0-3.5 10.9V17h7v-3.1A6 6 0 0 0 12 3zM9.5 20h5"/><path d="M12 0v1M3 9H2M22 9h-1"/></svg><p class="copy"><strong>Lorem ipsum dolor</strong><br>Lorem ipsum dolor sit amet, consectetur adipiscing elit, sed do eiusmod tempor</p></div>
      <div class="icon-cell"><svg viewBox="0 0 24 24" fill="none" stroke="#333" stroke-width="1.6"><circle cx="12" cy="12" r="7"/><circle cx="12" cy="12" r="2.5"/><path d="M12 1v6M12 17v6M1 12h6M17 12h6"/></svg><p class="copy"><strong>Lorem ipsum dolor</strong><br>Lorem ipsum dolor sit amet, consectetur adipiscing elit, sed do eiusmod tempor</p></div>
      <div class="icon-cell"><svg viewBox="0 0 24 24" fill="none" stroke="#333" stroke-width="1.6"><circle cx="15" cy="9" r="4"/><circle cx="7" cy="16" r="3"/><path d="M15 3v2M15 13v2M9 9h2M19 9h2"/></svg><p class="copy"><strong>Lorem ipsum dolor</strong><br>Lorem ipsum dolor sit amet, consectetur adipiscing elit, sed do eiusmod tempor</p></div>
      <div class="icon-cell"><svg viewBox="0 0 24 24" fill="none" stroke="#333" stroke-width="1.6"><path d="M12 3a6 6 0 0 0-3.5 10.9V17h7v-3.1A6 6 0 0 0 12 3zM9.5 20h5"/><path d="M12 0v1M3 9H2M22 9h-1"/></svg><p class="copy"><strong>Lorem ipsum dolor</strong><br>Lorem ipsum dolor sit amet, consectetur adipiscing elit, sed do eiusmod tempor</p></div>
    </div>
    <div class="footer-logo"><i></i>qTorvanix</div>
  </section>

  <!-- Photo header with text -->
  <section class="slide">
    <div class="photo" style="left:0;top:0;width:598px;height:206px;background:linear-gradient(140deg,#8c8a86,#4c4a47 55%,#2e2d2b)" role="img" aria-label="Photo of hands typing on a laptop"></div>
    <h2 class="title" style="top:70px;color:#fff;font-size:24px">Lorem ipsum dolor</h2>
    <p class="copy" style="position:absolute;left:28px;top:222px;width:170px">Lorem ipsum dolor sit amet, consectetur adipiscing elit, sed do eiusmod tempor <u>amet, consectetur</u> incididunt ut labore et dolore magna aliqua. Lorem ipsum dolor sit amet, <u>consectetur adipiscing elit</u>.</p>
    <p class="copy" style="position:absolute;left:214px;top:222px;width:170px">Lorem ipsum dolor sit amet, consectetur adipiscing elit, sed do eiusmod tempor incididunt ut labore et dolore magna aliqua. <u>amet, consectetur adipiscing elit</u>, sed do eiusmod tempor.</p>
    <p class="copy" style="position:absolute;left:400px;top:222px;width:170px">Lorem ipsum dolor sit amet, consectetur adipiscing elit, sed do eiusmod tempor <u>amet, consectetur</u> incididunt ut labore et dolore magna aliqua. Lorem ipsum dolor sit amet, <u>consectetur elit</u>.</p>
  </section>

  <!-- Pricing -->
  <section class="slide">
    <h2 class="title" style="top:26px;color:var(--green)">Sales proposals</h2>
    <table class="price-table">
      <thead><tr><th class="c1">Lorem ipsum dolor</th><th class="c2">Lorem ipsum dolor</th><th class="c3">Lorem ipsum dolor</th><th class="c4">Lorem ipsum dolor</th></tr></thead>
      <tbody>
        <tr class="plan"><td>Free</td><td>$9.90/month</td><td>$29.90/month</td><td>$59.90/month</td></tr>
        <tr><td>1</td><td>2</td><td>3</td><td>4</td></tr>
        <tr><td>3500</td><td>4250</td><td>6000</td><td>Unlimited</td></tr>
        <tr><td>1Gb</td><td>2Gb</td><td>5Gb</td><td>Unlimited</td></tr>
        <tr><td>Lorem</td><td>Lorem</td><td>Lorem</td><td>Lorem</td></tr>
      </tbody>
    </table>
    <div class="price-band"></div>
  </section>

  <!-- Timeline -->
  <section class="slide">
    <h2 class="title" style="top:26px">Operations <em>Plan</em></h2>
    <div class="timeline-line"></div>
    <div class="timeline">
      <div class="tl-step"><span class="tl-year">2015</span><div class="tl-dot"></div><div class="tl-stem"></div><p class="copy"><strong>Lorem ipsum dolor</strong><br>Lorem ipsum dolor sit amet, consectetur adipiscing elit, sed do eiusmod tempor</p></div>
      <div class="tl-step"><span class="tl-year">2016</span><div class="tl-dot"></div><div class="tl-stem"></div><p class="copy"><strong>Lorem ipsum dolor</strong><br>Lorem ipsum dolor sit amet, consectetur adipiscing elit, sed do eiusmod tempor</p></div>
      <div class="tl-step"><span class="tl-year">2017</span><div class="tl-dot"></div><div class="tl-stem"></div><p class="copy"><strong>Lorem ipsum dolor</strong><br>Lorem ipsum dolor sit amet, consectetur adipiscing elit, sed do eiusmod tempor</p></div>
      <div class="tl-step"><span class="tl-year">2018</span><div class="tl-dot"></div><div class="tl-stem"></div><p class="copy"><strong>Lorem ipsum dolor</strong><br>Lorem ipsum dolor sit amet, consectetur adipiscing elit, sed do eiusmod tempor</p></div>
      <div class="tl-step"><span class="tl-year">2019</span><div class="tl-dot"></div><div class="tl-stem"></div><p class="copy"><strong>Lorem ipsum dolor</strong><br>Lorem ipsum dolor sit amet, consectetur adipiscing elit, sed do eiusmod tempor</p></div>
    </div>
  </section>

  <!-- Team -->
  <section class="slide">
    <h2 class="title" style="top:16px">Our team</h2>
    <div class="team-band"></div>
    <div class="team">
      <div class="member"><div class="avatar" style="background:#e8653a" role="img" aria-label="Illustrated portrait of the chief executive"></div><p class="name">INSERT NAME</p><p class="role">CEO</p><p class="copy">Lorem ipsum dolor sit <u>amet, consectetur adipiscing</u></p></div>
      <div class="member"><div class="avatar" style="background:#c9a6d4" role="img" aria-label="Illustrated portrait of the head manager"></div><p class="name">INSERT NAME</p><p class="role">Head Manager</p><p class="copy">Lorem ipsum dolor sit amet, <u>amet, consectetur adipiscing elit.</u></p></div>
      <div class="member"><div class="avatar" style="background:#e9e9e9" role="img" aria-label="Illustrated portrait of the public relations lead"></div><p class="name">INSERT NAME</p><p class="role">Public Relation</p><p class="copy">Lorem ipsum dolor sit <u>amet, consectetur adipiscing elit.</u></p></div>
    </div>
  </section>

  <!-- Pills -->
  <section class="slide">
    <h2 class="title" style="top:18px">Lorem ipsum <em>dolor</em></h2>
    <div class="copy" style="position:absolute;left:28px;top:94px;width:150px"><strong style="font-size:7.5px">Lorem ipsum dolor</strong><br>Lorem ipsum dolor sit amet, <u>consectetur adipiscing</u> elit, sed do eiusmod tempor incididunt ut labore et dolore magna aliqua. Ut enim ad minim veniam, quis <u>amet, consectetur adipiscing elit</u>, sed do eiusmod tempor. Lorem ipsum dolor sit amet, <u>consectetur adipiscing elit</u>, sed do eiusmod tempor.</div>
    <div class="pill-list">
      <div class="pill p1"><span>1</span>It's where your clients are.</div>
      <div class="pill p2"><span>2</span>It's how they encounter new products,<br>services, and businesses.</div>
      <div class="pill p3"><span>3</span>It's where they share their lives.</div>
    </div>
  </section>

  <!-- Venn -->
  <section class="slide">
    <h2 class="title" style="top:16px">Lorem ipsum <em>dolor</em></h2>
    <svg class="venn" viewBox="0 0 240 250" aria-hidden="true">
      <circle cx="120" cy="80" r="72" fill="#6f8f33" fill-opacity="0.92"/>
      <circle cx="78" cy="170" r="72" fill="#a9c57a" fill-opacity="0.85"/>
      <circle cx="162" cy="170" r="72" fill="#5a7a25" fill-opacity="0.88"/>
    </svg>
    <p class="venn-label" style="left:116px;top:108px;width:100px">Consistent and<br>relevant<br>posting</p>
    <p class="venn-label" style="left:56px;top:212px;width:84px">Contests,<br>promotions,<br>and calls to<br>action</p>
    <p class="venn-label" style="left:168px;top:218px;width:90px">Custom social<br>media posts<br>and content</p>
    <p class="copy" style="position:absolute;left:356px;top:144px;width:200px">Lorem ipsum dolor sit amet, consectetur adipiscing elit, sed do eiusmod tempor incididunt ut labore et dolore magna aliqua. Ut enim ad minim veniam, quis nostrud exercitation ullamco laboris nisi ut aliquip ex ea commodo consequat. Lorem ipsum dolor sit amet, consectetur adipiscing elit, sed do eiusmod tempor incididunt ut labore et dolore magna aliqua. Lorem ipsum dolor sit amet.</p>
    <div class="footer-logo"><i></i>qTorvanix</div>
  </section>

  <!-- Thank you -->
  <section class="slide">
    <div class="photo" style="inset:0;background:linear-gradient(135deg,#c9c9c6,#8d8f90 50%,#5c5f62)" role="img" aria-label="Photo of a desk with a notebook, phone and glasses"></div>
    <div class="thanks-panel">
      <div class="thanks-mark"><i></i></div>
      <p class="thanks-word">THANK YOU</p>
      <p class="thanks-logo">qTorvanix</p>
    </div>
  </section>

</main>
</body>
</html>
```